Falverino’s Artisan Pizzeria Menu Contest

I’m looking for a menu design for a new pizzeria - it’s farm to table type of restaurant - more upscale than a typical pizzeria - white washed wood interior with some industrial accents - I am looking for a creative menu layout using the attached sample menu items -
Falverino’s is an artisanal pizzeria with an atmosphere that will make you feel at home for any situation, first date, anniversary, business lunch, boys night out or girls night out with a menu inspired by the idea of a simple honest cooking paired with fresh – quality ingredients. Full service dining experience that is still casual but dedicated to extraordinary hospitality.
While developing the menu we have created a network of amazing farms and purveyors to supply our restaurant with fresh milled 100% California flour for our hand crafted dough, as well as sustainably farmed organic produce, meats and cheeses.
The menu includes classics like the Margherita pizza to daily seasonal specials, fresh salads to rustic small plates including moms meatball recipe to a fresh local burrata with handmade bread. Each dish reflects our passion for sourcing the freshest quality local ingredients.
To compliment the menu, Falverino’s serves an extensive wine list with selections focusing on Italian varietals. The cocktail program has been carefully crafted to offer something to entice ever palate and the beer list has unique selections of the world’s finest brewers.
Target Market(s)
25-45 year old men and women
Industry/Entity Type
American Restaurant
Requirements
Must have
- professional tone
Nice to have
- a balance of elegance and industrial (rustic)
Should not have
- photos or playful graphics etc..

```html
<!DOCTYPE html>
<html lang="en">
<head>
<meta charset="utf-8">
<title>Falverino’s Menu</title>
<link rel="stylesheet" href="https://fonts.googleapis.com/css2?family=Crimson+Pro:wght@400;500&family=Playball&display=swap">
<style>
  :root {
    --ink: #1b1b1b;
    --accent: #e0575b;
    --paper: #ffffff;
  }
  * { box-sizing: border-box; margin: 0; padding: 0; }
  html, body { width: 848px; height: 1200px; overflow: hidden; background: var(--paper); }
  body { font-family: "Crimson Pro", Georgia, serif; color: var(--ink); }
  .menu { position: relative; width: 848px; height: 1200px; }

  .brand {
    position: absolute; left: 64px; top: 52px; width: 190px;
    font-size: 40px; font-weight: 500; line-height: 1; text-align: center; color: var(--ink);
  }
  .title {
    position: absolute; left: 297px; top: 30px; width: 233px;
    font-family: "Playball", cursive; font-size: 78px; line-height: 1;
    text-align: center; border-bottom: 2px solid var(--ink); padding-bottom: 6px;
  }
  .contact {
    position: absolute; left: 566px; top: 38px;
    font-size: 38px; line-height: 48px; font-weight: 400;
  }

  .section {
    position: absolute; border: 2px solid var(--accent);
  }
  .section-title {
    position: absolute; top: -20px; left: 50%; transform: translateX(-50%);
    background: var(--paper); padding: 0 14px; white-space: nowrap;
    font-size: 28px; font-weight: 400; color: var(--accent); line-height: 36px;
  }
  .sub-title {
    font-size: 26px; font-weight: 400; color: var(--accent); text-align: center; line-height: 32px;
  }
  .items { list-style: none; padding: 0 25px 0 27px; }
  .item { margin-bottom: 4px; }
  .item-head { display: flex; justify-content: space-between; line-height: 13.6px; }
  .item-name { font-size: 11.5px; font-weight: 500; }
  .item-price { font-size: 11.5px; }
  .item-desc { font-size: 10px; line-height: 13.6px; max-width: 232px; }
  .items.tight .item { margin-bottom: 0; }

  .appetizers { left: 59px; top: 180px; width: 328px; height: 285px; }
  .appetizers .items { margin-top: 50px; }
  .salads { left: 61px; top: 526px; width: 327px; height: 295px; }
  .salads .items { margin-top: 59px; }
  .sandwiches { left: 63px; top: 880px; width: 326px; height: 299px; }
  .sandwiches .items { margin-top: 71px; }
  .soup {
    left: 460px; top: 180px; width: 327px; height: 216px;
    display: flex; justify-content: space-between; align-items: center; padding: 0 32px 0 34px;
    color: var(--accent); font-size: 28px; font-weight: 500;
  }
  .pizzas { left: 460px; top: 458px; width: 327px; height: 721px; }
  .pizzas > .items { margin-top: 51px; }
  .pizzas .item-desc { max-width: 240px; }
  .crusts { margin-top: 18px; }
  .crusts .items { margin-top: 10px; }
  .crusts .item-desc { max-width: 120px; }
  .dips { margin-top: 10px; }
  .dips .items { margin-top: 18px; }
  .dips .item-head { line-height: 14.5px; }
</style>
</head>
<body>
<main class="menu">
  <div class="brand">Falverino’s</div>
  <h1 class="title">MENU</h1>
  <div class="contact">Adress<br>Phone number</div>

  <section class="section appetizers">
    <h2 class="section-title">Appetizers</h2>
    <ul class="items">
      <li class="item"><div class="item-head"><span class="item-name">Brussels</span><span class="item-price">$10,00</span></div><p class="item-desc">Pan seared brussel sprouts with a drizzle of balsamic reduction and parm and bread crumbs</p></li>
      <li class="item"><div class="item-head"><span class="item-name">Meatballs</span><span class="item-price">$13,00</span></div><p class="item-desc">Moms meatballs handmade secret recipe for over 75 years</p></li>
      <li class="item"><div class="item-head"><span class="item-name">Mussels</span><span class="item-price">$15,00</span></div><p class="item-desc">New Zealand Mussels in a tomato broth</p></li>
      <li class="item"><div class="item-head"><span class="item-name">Romanesco</span><span class="item-price">$11,00</span></div><p class="item-desc">Flash fried romanesco served atop a spicy aioli</p></li>
      <li class="item"><div class="item-head"><span class="item-name">Chicken wings</span><span class="item-price">$10,00</span></div><p class="item-desc">Italian fried chicken wings with a kick</p></li>
      <li class="item"><div class="item-head"><span class="item-name">Burrata</span><span class="item-price">$13,00</span></div><p class="item-desc">Local burrata served with apples grapes and fresh made bread</p></li>
    </ul>
  </section>

  <section class="section soup">
    <span class="soup-name">Daily Soup</span>
    <span class="soup-price">$8,00</span>
  </section>

  <section class="section salads">
    <h2 class="section-title">Salads</h2>
    <ul class="items">
      <li class="item"><div class="item-head"><span class="item-name">Chopped Salad</span><span class="item-price">$13,00</span></div><p class="item-desc">Lettuce mix with tomato, onions, peppers, pepperoni, chick peas, fresh mozz, italian herb ving</p></li>
      <li class="item"><div class="item-head"><span class="item-name">Caesar Salad</span><span class="item-price">$11,00</span></div><p class="item-desc">Traditional caesar salad rich and creamy extra shaved parmesan</p></li>
      <li class="item"><div class="item-head"><span class="item-name">Farm Salad</span><span class="item-price">$15,00</span></div><p class="item-desc">Seasonal farmers market salad</p></li>
      <li class="item"><div class="item-head"><span class="item-name">Grilled Little Gem</span><span class="item-price">$11,00</span></div><p class="item-desc">Grilled little gems with bacon, tomato, red onions and blue cheese dressing</p></li>
      <li class="item"><div class="item-head"><span class="item-name">Spinach and Arugula Salad</span><span class="item-price">$12,00</span></div><p class="item-desc">Spinach and argula, red pepperstossed in a lemon ving and housemade croutons</p></li>
    </ul>
  </section>

  <section class="section sandwiches">
    <h2 class="section-title">Sandwiches</h2>
    <ul class="items">
      <li class="item"><div class="item-head"><span class="item-name">Italian sub</span><span class="item-price">$13,00</span></div><p class="item-desc">Prociutto, salumi, turkey, provolone, lettuce, tomato and herb aioli with spicy gardenia</p></li>
      <li class="item"><div class="item-head"><span class="item-name">Turkey sandwich</span><span class="item-price">$12,00</span></div><p class="item-desc">Housemade bread - turkey, cheddar cheese, butter lettuce, tomato and mustard aioli</p></li>
      <li class="item"><div class="item-head"><span class="item-name">Meatball sub</span><span class="item-price">$13,00</span></div><p class="item-desc">Moms meatballs melted provolone on a housemade roll</p></li>
      <li class="item"><div class="item-head"><span class="item-name">Evergreen burger</span><span class="item-price">$14,00</span></div><p class="item-desc">Housemade bun - arugula , tomato, onion and a sundried tomato spread</p></li>
      <li class="item"><div class="item-head"><span class="item-name">Chicken sandwich</span><span class="item-price">$13,00</span></div><p class="item-desc">Fried chicken or chicken breast, provolone, argula, tomato, served with a spicy aioli</p></li>
    </ul>
  </section>

  <section class="section pizzas">
    <h2 class="section-title">Pizzas</h2>
    <ul class="items">
      <li class="item"><div class="item-head"><span class="item-name">Margherita</span><span class="item-price">$14,00</span></div><p class="item-desc">Classic Margherita pizza - Fresh Mozz Tomato Sauce and Basil</p></li>
      <li class="item"><div class="item-head"><span class="item-name">Organic Sausage</span><span class="item-price">$16,00</span></div><p class="item-desc">Organic Sausage Housemade Red Sauce Mozz hint of fennel</p></li>
      <li class="item"><div class="item-head"><span class="item-name">Pepperoni</span><span class="item-price">$16,00</span></div><p class="item-desc">Harlow Pepperoni - Housemade Red Sauce Chile flakes and Mozz</p></li>
      <li class="item"><div class="item-head"><span class="item-name">Salumi and Burrata</span><span class="item-price">$17,00</span></div><p class="item-desc">Salumi dried Red Sauce finished with whipped burrata</p></li>
      <li class="item"><div class="item-head"><span class="item-name">Daily special</span><span class="item-price">$17,00</span></div></li>
      <li class="item"><div class="item-head"><span class="item-name">Mushroom</span><span class="item-price">$15,00</span></div><p class="item-desc">Shaved mushrooms with a Parmesan cream and melted onions</p></li>
      <li class="item"><div class="item-head"><span class="item-name">Prosciutto and egg</span><span class="item-price">$16,00</span></div><p class="item-desc">Parma Prosciutto Parmesan cream with Havarti and gruyere finished with an organic egg</p></li>
      <li class="item"><div class="item-head"><span class="item-name">Quarttro Formaggi</span><span class="item-price">$15,00</span></div><p class="item-desc">Four cheese combination - mozz - fontina - parm cream and gruyere chile flakes and oregano</p></li>
      <li class="item"><div class="item-head"><span class="item-name">Farmers Pizza</span><span class="item-price">$17,00</span></div><p class="item-desc">Seasonal vegatables cream sauce and a variety of cheese</p></li>
      <li class="item"><div class="item-head"><span class="item-name">Keto friendly</span><span class="item-price">$17,00</span></div><p class="item-desc">Cauliflower crust, spinach and kale , parm cream sauce</p></li>
    </ul>

    <div class="crusts">
      <h3 class="sub-title">Crusts</h3>
      <ul class="items">
        <li class="item"><div class="item-head"><span class="item-name">Traditional</span></div><p class="item-desc">Original crust you can’t miss</p></li>
        <li class="item"><div class="item-head"><span class="item-name">Gluten free</span><span class="item-price">$3,00</span></div><p class="item-desc">Best gluten friendly crust on the west coast</p></li>
        <li class="item"><div class="item-head"><span class="item-name">Cauliflower</span><span class="item-price">$3,00</span></div><p class="item-desc">Vegans have needs</p></li>
      </ul>
    </div>

    <div class="dips">
      <h3 class="sub-title">Dips</h3>
      <ul class="items tight">
        <li class="item"><div class="item-head"><span class="item-name">Ranch</span><span class="item-price">$1,00</span></div></li>
        <li class="item"><div class="item-head"><span class="item-name">Tomato sauce</span><span class="item-price">$1,00</span></div></li>
        <li class="item"><div class="item-head"><span class="item-name">Spicy dip</span><span class="item-price">$1,00</span></div></li>
        <li class="item"><div class="item-head"><span class="item-name">Blue cheese</span><span class="item-price">$1,00</span></div></li>
      </ul>
    </div>
  </section>
</main>
</body>
</html>
```